Investment company needing business card

We are wanting a business card which looks sharp and easy on the eye. We are thinking of having a business card with the logo embossed on it, to really make it stand out. We will only have a small amount of information of the business card, person's name, position, email address and phone number

Contact Information for Business Card

Danica Pruett
Executive Assistant
+64 21 547 3162
danicap@harwellcapital.co.nz

Requirements
Must have
• Embossed logo
Should not have
• Not to be busy

```html
<!DOCTYPE html>
<html lang="en">
<head>
<meta charset="utf-8">
<title>Harwell Capital – Business Card</title>
<link href="https://fonts.googleapis.com/css2?family=Fira+Sans:wght@400;600&display=swap" rel="stylesheet">
<style>
  :root {
    --backdrop: #e6e2dd;
    --card: #f4f2ee;
    --brand-green: #2ea866;
    --ink-grey: #5a5a5a;
    --mark-grey: #4f4f4f;
    --deboss: #dcd9d3;
  }
  html, body {
    margin: 0;
    width: 1200px;
    height: 1078px;
    overflow: hidden;
    background: var(--backdrop);
  }
  .card {
    position: absolute;
    left: 100px;
    top: 249px;
    width: 1000px;
    height: 580px;
    background: var(--card);
    border-radius: 4px;
    font-family: "Fira Sans", sans-serif;
  }
  .identity {
    position: absolute;
    left: 96px;
    top: 84px;
    display: flex;
    align-items: center;
    gap: 48px;
  }
  .identity__mark {
    width: 64px;
    height: 64px;
    background: var(--brand-green);
  }
  .identity__name {
    margin: 0;
    font-weight: 600;
    font-size: 44px;
    color: var(--brand-green);
    line-height: 1.1;
  }
  .identity__role {
    margin: 4px 0 0;
    font-weight: 400;
    font-size: 31px;
    color: var(--ink-grey);
  }
  .company-name {
    position: absolute;
    left: 0;
    right: 0;
    top: 226px;
    text-align: center;
    font-weight: 400;
    font-size: 84px;
    letter-spacing: 4px;
    color: var(--deboss);
    text-transform: uppercase;
  }
  .contact {
    position: absolute;
    left: 170px;
    top: 418px;
    display: flex;
    align-items: center;
    gap: 48px;
  }
  .contact__mark {
    width: 64px;
    height: 64px;
    background: var(--mark-grey);
  }
  .contact__line {
    margin: 0;
    font-size: 30px;
    color: var(--ink-grey);
    line-height: 1.3;
  }
</style>
</head>
<body>
  <main class="card">
    <div class="identity">
      <div class="identity__mark"></div>
      <div>
        <p class="identity__name">Danica Pruett</p>
        <p class="identity__role">Executive Assistant</p>
      </div>
    </div>

    <div class="company-name">Harwell Capital</div>

    <div class="contact">
      <div class="contact__mark"></div>
      <div>
        <p class="contact__line">+64 21 547 3162</p>
        <p class="contact__line">danicap@harwellcapital.co.nz</p>
      </div>
    </div>
  </main>
</body>
</html>
```